Fitness competition business needs a card design

I need a professional business card design using my logo. The card will be horizontal with rounded edges.

Target Market(s)

Female fitness competitors

Industry/Entity Type

Fitness

Contact Information for Business Card

Lise-Anne Korvath
Owner
stagevelora.com
210.555.0137
info@stagevelora.com

Font styles to use
Serif

Colors

Designer to choose colors to be used in the design.

Requirements
Must have
• On the back please add the following:
• Figure
• Bikini
• Physique
• Fitness
Nice to have
• Looking for a very sleek design, contemporary and easy to read.
Should not have
• Should not be difficult to read or be too busy

```html
<!DOCTYPE html>
<html lang="en">
<head>
<meta charset="utf-8">
<title>Stage Velora – Business Card</title>
<link rel="stylesheet" href="https://fonts.googleapis.com/css2?family=Playfair+Display:wght@700&family=Lora:wght@400;600&display=swap">
<style>
  :root {
    --backdrop: #2a2a2b;
    --paper: #f1f1f1;
    --brand-red: #ec2027;
    --rule-grey: #58595b;
    --back-grey: #5f6062;
    --mark-grey: #6c6d70;
    --ink-white: #ffffff;
    --soft-white: #e6e6e7;
  }
  * { margin: 0; padding: 0; box-sizing: border-box; }
  html, body {
    width: 1200px; height: 960px; overflow: hidden;
    background: var(--backdrop);
  }
  .stage { position: relative; width: 1200px; height: 960px; }
  .card {
    position: absolute; width: 600px; height: 342px;
    border-radius: 22px; overflow: hidden;
  }
  .card-front { left: 314px; top: 113px; background: var(--paper); }
  .card-back { left: 311px; top: 472px; background: var(--back-grey); }
  .card-art { position: absolute; inset: 0; display: block; }

  .brand-name {
    position: absolute; left: 0; right: 0; top: 120px;
    text-align: center;
    font-family: "Playfair Display", serif; font-weight: 700;
    font-size: 36px; line-height: 44px; letter-spacing: 1px;
    color: var(--brand-red);
  }
  .contact-block {
    position: absolute; left: 0; right: 0; top: 236px;
    text-align: center; color: var(--ink-white);
    font-family: "Lora", serif;
  }
  .person-name {
    font-family: "Playfair Display", serif; font-weight: 700;
    font-size: 20px; line-height: 26px; letter-spacing: 0.5px;
  }
  .person-role {
    font-weight: 600; font-size: 13px; line-height: 20px;
    letter-spacing: 1px; margin-bottom: 7px;
  }
  .contact-line { font-size: 14px; line-height: 20px; }
  .web-line { font-size: 14px; line-height: 20px; letter-spacing: 2.4px; }

  .category-list {
    position: absolute; right: 32px; top: 34px;
    list-style: none; text-align: right;
    font-family: "Lora", serif; font-weight: 600;
    font-size: 16px; line-height: 30px; letter-spacing: 3px;
    color: var(--soft-white);
  }
  .back-brand {
    position: absolute; right: 32px; bottom: 48px;
    font-family: "Playfair Display", serif; font-weight: 700;
    font-size: 32px; line-height: 40px; letter-spacing: 1px;
    color: var(--ink-white); text-align: right;
  }
  .back-web {
    position: absolute; right: 32px; bottom: 18px;
    font-family: "Lora", serif; font-size: 14px;
    letter-spacing: 2.2px; color: var(--ink-white);
  }
</style>
</head>
<body>
<main class="stage">
  <section class="card card-front">
    <svg class="card-art" viewBox="0 0 600 342" aria-hidden="true">
      <path d="M0 120 Q300 314 600 120 L600 342 L0 342 Z" fill="var(--brand-red)"/>
      <path d="M0 120 Q300 314 600 120" fill="none" stroke="var(--rule-grey)" stroke-width="4"/>
    </svg>
    <div class="brand-name">STAGE VELORA</div>
    <div class="contact-block">
      <p class="person-name">LISE-ANNE KORVATH</p>
      <p class="person-role">OWNER</p>
      <p class="contact-line">P. 210.555.0137 E . info@stagevelora.com</p>
      <p class="web-line">www.stagevelora.com</p>
    </div>
  </section>

  <section class="card card-back">
    <svg class="card-art" viewBox="0 0 600 342" aria-hidden="true">
      <circle cx="130" cy="150" r="140" fill="var(--mark-grey)"/>
    </svg>
    <ul class="category-list">
      <li>FIGURE</li>
      <li>BIKINI</li>
      <li>PHYSIQUE</li>
      <li>FITNESS</li>
    </ul>
    <div class="back-brand">STAGE VELORA</div>
    <div class="back-web">www.stagevelora.com</div>
  </section>
</main>
</body>
</html>
```